Mexican construction company needs a business card design

We need a business card design for a company based in Monterrey, Mexico called:

Desarrollos Tolvani S.A. de C.V.

The company is in the construction business and I would like the businees card to be simple and concise. Please use white background and blue or black text color that say:

"Proyectos de Construcción"-- (Brief description of business)
" Rodrigo Ulloa Benítez"--- (My name)
"rulloab@correovelo.mx"-- (My email)
"C: (81) 82 19 57 46"-- (My cell)
"O: (81) 86 72 13 95"-- (Office phone)

Please use only the colors of my company that are attached

Please make the back of the business card blue (same blue from logo) and use the logo.

Thanks!

```html
<!DOCTYPE html>
<html lang="es">
<head>
<meta charset="utf-8">
<title>Desarrollos Tolvani – Tarjeta de presentación</title>
<link rel="stylesheet" href="https://fonts.googleapis.com/css2?family=Oswald:wght@400&family=Noto+Sans:ital,wght@0,400;0,500;1,400&display=swap">
<style>
  :root {
    --backdrop: #e9e6e2;
    --card: #ffffff;
    --navy: #221d5e;
    --navy-deep: #19154a;
    --silver-light: #e4e4ea;
    --silver-dark: #9a9aa6;
    --ink: #1d1a45;
    --ink-soft: #2c2c38;
    --icon: #6d6d78;
  }
  * { margin: 0; padding: 0; box-sizing: border-box; }
  html, body {
    width: 1200px; height: 970px; overflow: hidden;
    background: var(--backdrop);
  }
  .business-card {
    position: absolute; left: 120px; top: 218px;
    width: 960px; height: 534px;
    background: var(--card);
    box-shadow: 0 10px 30px rgba(0,0,0,.12);
    overflow: hidden;
  }
  .brand-panel { position: absolute; inset: 0; width: 960px; height: 534px; }
  .brand-name {
    position: absolute; left: 0; width: 470px; top: 292px;
    text-align: center;
    font-family: "Noto Sans", sans-serif; font-weight: 500;
    color: var(--silver-light); text-transform: uppercase;
  }
  .brand-name .line-top { display: block; font-size: 27px; letter-spacing: 3px; }
  .brand-name .line-main { display: block; font-size: 40px; letter-spacing: 4px; margin-top: 2px; }
  .contact-block { position: absolute; left: 578px; top: 142px; }
  .person-name {
    font-family: "Oswald", sans-serif; font-weight: 400;
    font-size: 27px; color: var(--ink); letter-spacing: .3px;
  }
  .contact-list { list-style: none; margin-top: 28px; }
  .contact-list li {
    display: flex; align-items: center; height: 34px;
    font-family: "Noto Sans", sans-serif; font-size: 21px; color: var(--ink-soft);
  }
  .contact-list svg { width: 24px; height: 22px; margin-right: 27px; fill: var(--icon); }
  .tagline {
    margin-top: 30px;
    font-family: "Noto Sans", sans-serif; font-style: italic;
    font-size: 20px; color: var(--ink-soft);
  }
</style>
</head>
<body>
  <div class="business-card">
    <svg class="brand-panel" viewBox="0 0 960 534" aria-hidden="true">
      <defs>
        <linearGradient id="silverEdge" x1="0" y1="0" x2="0" y2="1">
          <stop offset="0" stop-color="var(--silver-light)"/>
          <stop offset=".5" stop-color="var(--silver-dark)"/>
          <stop offset="1" stop-color="var(--silver-light)"/>
        </linearGradient>
        <linearGradient id="navyFill" x1="0" y1="0" x2="1" y2="1">
          <stop offset="0" stop-color="var(--navy)"/>
          <stop offset="1" stop-color="var(--navy-deep)"/>
        </linearGradient>
      </defs>
      <path d="M0 0 H478 C535 120 535 260 515 360 C500 440 475 500 461 534 H0 Z" fill="url(#silverEdge)"/>
      <path d="M0 0 H463 C520 120 520 260 500 360 C485 440 460 500 446 534 H0 Z" fill="url(#navyFill)"/>
    </svg>

    <div class="brand-name">
      <span class="line-top">Desarrollos</span>
      <span class="line-main">Tolvani</span>
    </div>

    <div class="contact-block">
      <h1 class="person-name">Rodrigo Ulloa Benítez</h1>
      <ul class="contact-list">
        <li>
          <svg viewBox="0 0 24 22" aria-label="Teléfono de oficina"><path d="M3 7 C3 3 21 3 21 7 L21 9 L16 9 L16 7 L8 7 L8 9 L3 9 Z M7 10 H17 L20 19 H4 Z"/></svg>
          (81) 86 72 13 95
        </li>
        <li>
          <svg viewBox="0 0 24 22" aria-label="Celular"><path d="M7 0 H17 A2 2 0 0 1 19 2 V20 A2 2 0 0 1 17 22 H7 A2 2 0 0 1 5 20 V2 A2 2 0 0 1 7 0 Z M7 3 V17 H17 V3 Z M11 18.5 H13 V20.5 H11 Z"/></svg>
          (81) 82 19 57 46
        </li>
        <li>
          <svg viewBox="0 0 24 22" aria-label="Correo"><path d="M1 4 H23 L12 12 Z M1 6 L12 14 L23 6 V18 H1 Z"/></svg>
          rulloab@correovelo.mx
        </li>
      </ul>
      <p class="tagline">Proyectos de Construcción</p>
    </div>
  </div>
</body>
</html>
```